We need help creating industry specific one page marketing flyers

We are kicking off a campaign to target specific industry verticals and need help creating / designing one pager marketing collateral for each industry.

See attached our first industry, healthcare. I created this but want to make it more professional looking.

Here is our website (the website is old, we're refreshing this in the near future). www.brookvane.com

I want it in powerpoint format so that I can make adjustments to the one pager and create PDFs from it as well.

Target Market(s)

Property managers and facilities managers

Industry/Entity Type

Industry

Requirements
Must have
• Tie to our corporate logo colors
• Use plant pictures and visuals to tell the story
• Must be in an editable format (e.g. powerpoint) so I can make tweaks to the content

```html
<!DOCTYPE html>
<html lang="en">
<head>
<meta charset="utf-8">
<title>Brookvane – Indoor Plants for Healthcare Facilities</title>
<link rel="stylesheet" href="https://fonts.googleapis.com/css2?family=Marcellus&family=Raleway:wght@400;600;700;800&family=Open+Sans:wght@400;700&display=swap">
<style>
  :root {
    --band-green: #93b69c;
    --brand-green: #6aaa3a;
    --tick-green: #7cb868;
    --rule-green: #9dbca5;
    --ink: #1d1d1d;
    --soft-ink: #333333;
    --grey-band: #efefef;
    --paper: #ffffff;
  }
  * { box-sizing: border-box; margin: 0; padding: 0; }
  html, body { width: 857px; height: 1200px; overflow: hidden; background: var(--paper); }
  .flyer { position: relative; width: 857px; height: 1200px; background: var(--paper); overflow: hidden; font-family: "Open Sans", sans-serif; color: var(--ink); }

  .band { position: absolute; left: 0; width: 100%; background: var(--band-green); }
  .band--top { top: 0; height: 22px; }
  .band--bottom { bottom: 0; height: 30px; }

  .brand { position: absolute; top: 92px; left: 0; width: 100%; display: flex; justify-content: center; align-items: center; gap: 14px; }
  .brand__name { font-family: "Marcellus", serif; font-size: 66px; color: var(--brand-green); line-height: 1; }
  .brand__dot { width: 22px; height: 22px; border-radius: 50%; background: var(--brand-green); margin-top: -38px; }

  .tagline { position: absolute; top: 178px; left: 0; width: 100%; text-align: center; font-family: "Raleway", sans-serif; font-size: 19px; letter-spacing: 1.6px; color: var(--soft-ink); }

  .welcome { position: absolute; top: 211px; left: 0; width: 100%; height: 57px; background: var(--grey-band); display: flex; align-items: center; padding-left: 76px; gap: 14px; }
  .welcome__text { font-family: "Raleway", sans-serif; font-size: 20px; letter-spacing: 2px; color: var(--brand-green); }

  .photo { position: absolute; top: 277px; height: 434px; }
  .photo--lounge { left: 0; width: 553px; background: linear-gradient(180deg, #eceeed 0%, #e4e7e4 45%, #c9d3c2 70%, #dfe2df 100%); }
  .photo--pots { left: 553px; width: 304px; background: linear-gradient(180deg, #f3f3f2 0%, #eef0ec 50%, #dfe5d8 75%, #f5f5f4 100%); }

  .column__heading { position: absolute; font-family: "Raleway", sans-serif; font-weight: 800; font-size: 23px; letter-spacing: 1.6px; text-align: center; line-height: 25px; color: var(--ink); }
  .column--left .column__heading { top: 719px; left: 0; width: 395px; }
  .column--right .column__heading { top: 724px; left: 460px; width: 365px; }

  .rule { position: absolute; height: 5px; background: var(--rule-green); }
  .column--left .rule { top: 784px; left: 54px; width: 291px; }
  .column--right .rule { top: 769px; left: 460px; width: 357px; }

  .ticks { position: absolute; list-style: none; }
  .ticks li { position: relative; color: var(--ink); }
  .ticks svg { position: absolute; left: 0; }
  .column--left .ticks { top: 810px; left: 14px; width: 330px; }
  .column--left .ticks li { padding-left: 25px; font-size: 16.5px; line-height: 36px; }
  .column--left .ticks svg { top: 10px; }
  .column--right .ticks { top: 800px; left: 479px; width: 378px; }
  .column--right .ticks li { padding-left: 26px; font-size: 17px; line-height: 31px; }
  .column--right .ticks svg { top: 8px; }

  .contact { position: absolute; top: 1052px; left: 0; width: 100%; text-align: center; font-family: "Open Sans", sans-serif; font-weight: 700; font-size: 18.7px; line-height: 28px; color: var(--ink); }

  .footer-brand { position: absolute; top: 1110px; left: 14px; display: flex; align-items: center; gap: 8px; }
  .footer-brand__name { font-family: "Marcellus", serif; font-size: 32px; color: var(--brand-green); line-height: 1; }
  .footer-brand__dot { width: 10px; height: 10px; border-radius: 50%; background: var(--brand-green); margin-top: -18px; }

  .address { position: absolute; top: 1101px; right: 18px; text-align: right; font-family: "Raleway", sans-serif; font-weight: 700; font-style: normal; font-size: 12px; letter-spacing: 1.5px; line-height: 16px; color: var(--ink); }
</style>
</head>
<body>
<main class="flyer">
  <div class="band band--top"></div>

  <header class="brand">
    <span class="brand__name">Brookvane</span>
    <span class="brand__dot"></span>
  </header>

  <p class="tagline">Indoor Plant Design and Maintenance Services for Healthcare Facilities</p>

  <div class="welcome">
    <svg width="26" height="26" viewBox="0 0 26 26" aria-hidden="true">
      <path d="M3 12 L13 3 L23 12" fill="none" stroke="#6aaa3a" stroke-width="2.4" stroke-linejoin="round"/>
      <rect x="6" y="11" width="14" height="12" fill="none" stroke="#6aaa3a" stroke-width="2.4"/>
      <rect x="11" y="15" width="4" height="8" fill="#6aaa3a"/>
    </svg>
    <span class="welcome__text">We can help you make your healthcare facility more welcoming!</span>
  </div>

  <div class="photo photo--lounge" role="img" aria-label="Bright white lounge with a grey sofa, a patterned cushion and tall potted palms and leafy plants around it"></div>
  <div class="photo photo--pots" role="img" aria-label="Several concrete planters of different heights holding small green leafy plants on a white floor"></div>

  <section class="column column--left">
    <h2 class="column__heading">WE KNOW HEALTHCARE<br>FACILITIES</h2>
    <div class="rule"></div>
    <ul class="ticks">
      <li><svg width="14" height="12" viewBox="0 0 14 12" aria-hidden="true"><path d="M1 6 L5 10 L13 1" fill="none" stroke="#7cb868" stroke-width="1.8"/></svg>&nbsp;We currently serve over 20 of the largest hospitals and healthcare facilities across the Bay Area</li>
      <li><svg width="14" height="12" viewBox="0 0 14 12" aria-hidden="true"><path d="M1 6 L5 10 L13 1" fill="none" stroke="#7cb868" stroke-width="1.8"/></svg>We understand what works in a hospital from using the right moss to minimize dusty to the right plant</li>
    </ul>
  </section>

  <section class="column column--right">
    <h2 class="column__heading">BENEFITS OF PLANTS</h2>
    <div class="rule"></div>
    <ul class="ticks">
      <li><svg width="14" height="12" viewBox="0 0 14 12" aria-hidden="true"><path d="M1 6 L5 10 L13 1" fill="none" stroke="#7cb868" stroke-width="1.8"/></svg>High impact amenity at a low cost</li>
      <li><svg width="14" height="12" viewBox="0 0 14 12" aria-hidden="true"><path d="M1 6 L5 10 L13 1" fill="none" stroke="#7cb868" stroke-width="1.8"/></svg>Create a calming environment for patients</li>
      <li><svg width="14" height="12" viewBox="0 0 14 12" aria-hidden="true"><path d="M1 6 L5 10 L13 1" fill="none" stroke="#7cb868" stroke-width="1.8"/></svg>Patients' stress levels increase in the hospital, however exposure to natural settings has the ability to reduce stress and enhance the process of healing</li>
      <li><svg width="14" height="12" viewBox="0 0 14 12" aria-hidden="true"><path d="M1 6 L5 10 L13 1" fill="none" stroke="#7cb868" stroke-width="1.8"/></svg>Are proven to provide health benefits such as cleaning indoor air</li>
    </ul>
  </section>

  <p class="contact">For a design consultation, please contact 510-555-0147 or &nbsp;Dana Whitlock at<br>whitlock@brookvane.com</p>

  <div class="footer-brand">
    <span class="footer-brand__name">Brookvane</span>
    <span class="footer-brand__dot"></span>
  </div>

  <address class="address">
    Brookvane, Inc.<br>
    PO Box 41720<br>
    Fremont, CA 94538<br>
    info@brookvane.com
  </address>

  <div class="band band--bottom"></div>
</main>
</body>
</html>
```